Business card - house cleaning company

We want friendly high end business card highlighting our services . NO LOGOs on back of card please.. no vertical cards NO DOUBLE BROOMS

2 owners of the company: Corinne Hale & Dean Oakley

Included phone number: (555)318-2207

Email: brightnookclean@example.net

Website: www.brightnookclean.example

Bonded & Insured

Pine Hollow, CO 80999

Slogan maybe: Bringing a brighter shine to every corner of home

We want elegant high end card for house cleaning service. Maybe 2 sided if needed. Can it have bullet points of some services we offer

Residential Home Cleaning
Vacation Rental Cleaning
Commercial Cleaning
Carpet Cleaning
Window Cleaning
Property Management
Property Inspections
Property Maintenance
Trash Removal
Concierge Services

Highlight service on back of card. If we can do a one sided card with all this that’s great as well. Not cartoony.

Our logo attached and a design somone I had Harlan but they put very little time in. Not Unique enough. If you can do a custom design with a feminine touch that be great.

You will be eliminated for not reading the brief. NO DOUBLE LOGOS NO DOUBLE BROOMS. PLEASE BE CREATIVE. IF POST SAME LOGO WITH SMAL CHANGES RHEY WILL BE ELIMINATED. BE CREATIVE.
Updates

Thank you everyone for your designs. please only use the logo 1 time. and would love to see some that dont look all the same. We appreciate your time.

Target Market(s)

Residential and vacation rental home cleaning maid service

Industry/Entity Type

House cleaning maid services

Contact Information for Business Card

For business card use logo. black and green one provided. others for example. I wil try find some example.. We want friendly high end look. 2 owners of the company: Corinne Hale & Dean Oakley Included phone number: (555)318-2207 Email: brightnookclean@example.net Website: www.brightnookclean.example Bonded & Insured Pine Hollow, CO Slogan maybe: Bringing a brighter shine to every corner of home or Quality Service Guaranteed We want elegant high end card for house cleaning service. Maybe 2 sided if needed. Can it have bullet points of some services we offer Residential Home Cleaning Vacation Rental Cleaning Commercial Cleaning Carpet Cleaning Window Cleaning Property Management Property Inspections Property Maintenance Trash Removal Concierge Services

Requirements
Must have
• For business card use logo . Creativity. black and green one provided. We want friendly high end look. 2 owners of the company: Corinne Hale & Dean Oakley Included phone number: (555)318-2207 Email: brightnookclean@example.net Website: www.brightnookclean.example Licensed Bonded & Insured Pine Hollow, CO Slogan maybe: Bringing a brighter shine to every corner of home or Quality Service Guaranteed We want elegant high end card for house cleaning service. Maybe 2 sided if needed. Can it have bullet points of some services we offer Residential Home Cleaning Vacation Rental Cleaning Commercial Cleaning Carpet Cleaning Window Cleaning Property Management Property Inspections Property Maintenance Trash Removal Concierge Services .. creatitivty a plus. whimsical. we like stars..
Nice to have
• we want much better than the example of biz card provided as example. logo has colors that are in our website palette as well. We are open to ideas for the business card design. Will pay tip to best work. PLEASE USE COMPLIMENTING COLORS. . WE LIKE BLACK AND WHITE, stars
Should not have
• NO DOUBLE LOGOS. READ READ. READ. YOU WILL BE ELIMINATED no double logos or double brooms same side of card. I want didfrent examples. please don't make all your submission look the same

```html
<!DOCTYPE html>
<html lang="en">
<head>
<meta charset="utf-8">
<title>Bright Nook Cleaning Services – Business Card</title>
<link rel="stylesheet" href="https://fonts.googleapis.com/css2?family=Gilda+Display&family=Cinzel:wght@600&family=Dancing+Script:wght@500&display=swap">
<style>
  :root {
    --backdrop: #6f964c;
    --leaf: #6f9a44;
    --ink: #111111;
    --card: #ffffff;
    --mist: #dcdcdc;
    --band: #efefef;
  }
  * { margin: 0; padding: 0; box-sizing: border-box; }
  html, body { width: 975px; height: 1200px; overflow: hidden; }
  body {
    background: var(--backdrop);
    position: relative;
    font-family: "Gilda Display", Georgia, serif;
    color: var(--ink);
  }
  .card {
    position: absolute;
    left: 85px;
    width: 805px;
    height: 483px;
    background: var(--card);
    box-shadow: 0 10px 28px rgba(0,0,0,.35);
    overflow: hidden;
  }
  .card--front { top: 85px; }
  .card--back { top: 639px; }
  .sparkle-field {
    position: absolute;
    left: 0; top: 0;
    width: 100%; height: 400px;
    background: radial-gradient(ellipse 70% 80% at 50% 0%, var(--mist) 0%, #ececec 45%, #ffffff 100%);
  }
  .center { position: absolute; left: 0; width: 100%; text-align: center; }
  .brand-name {
    top: 94px;
    font-size: 60px;
    font-weight: 400;
    line-height: 1;
    color: var(--ink);
    letter-spacing: .5px;
  }
  .brand-tagline {
    top: 158px;
    font-family: "Cinzel", serif;
    font-size: 20px;
    letter-spacing: 1.5px;
    color: var(--leaf);
  }
  .script-band {
    position: absolute;
    background: var(--leaf);
    border-radius: 22px;
    color: #fff;
    font-family: "Dancing Script", cursive;
    display: flex;
    align-items: center;
    justify-content: center;
    white-space: nowrap;
  }
  .script-band--slogan { left: 178px; top: 199px; width: 449px; height: 42px; font-size: 23px; }
  .script-band--promise { left: 262px; top: 82px; width: 283px; height: 48px; font-size: 26px; }
  .owners { top: 256px; font-size: 25px; }
  .phone-line {
    top: 299px;
    display: flex; justify-content: center; align-items: center; gap: 6px;
    font-size: 27px;
  }
  .icon-dot {
    display: inline-flex; align-items: center; justify-content: center;
    border-radius: 50%; background: var(--leaf);
  }
  .icon-dot--lg { width: 35px; height: 35px; }
  .icon-dot--sm { width: 23px; height: 23px; }
  .web-line {
    top: 354px;
    display: flex; justify-content: center; align-items: center; gap: 12px;
    font-size: 16.5px;
  }
  .web-line .divider { margin: 0 14px; color: var(--ink); }
  .info-band {
    position: absolute; left: 0; top: 398px; width: 100%; height: 32px;
    background: var(--band);
    display: flex; justify-content: center; align-items: center; gap: 8px;
  }
  .info-band--front { font-family: "Cinzel", serif; font-weight: 600; font-size: 15.5px; letter-spacing: .8px; }
  .info-band--back { font-size: 17px; top: 397px; }
  .services {
    position: absolute; top: 164px; list-style: none;
    font-size: 17px;
  }
  .services--left { left: 130px; }
  .services--right { left: 474px; }
  .services li { height: 34.4px; display: flex; align-items: center; gap: 14px; }
</style>
</head>
<body>

<section class="card card--front">
  <div class="sparkle-field" role="img" aria-label="Soft silver backdrop with scattered sparkle stars"></div>

  <h1 class="center brand-name">Bright Nook</h1>
  <p class="center brand-tagline">CLEANING SERVICES</p>

  <p class="script-band script-band--slogan">Bringing a brighter shine to every corner of home</p>

  <p class="center owners">Corinne Hale &amp; Dean Oakley</p>

  <p class="center phone-line">
    <span class="icon-dot icon-dot--lg">
      <svg width="14" height="20" viewBox="0 0 14 20"><rect x="2" y="1" width="10" height="18" rx="2" fill="none" stroke="#fff" stroke-width="1.6"/><circle cx="7" cy="16" r="1" fill="#fff"/></svg>
    </span>
    (555)318-2207
  </p>

  <p class="center web-line">
    <span class="icon-dot icon-dot--sm">
      <svg width="13" height="13" viewBox="0 0 14 14"><circle cx="7" cy="7" r="5.5" fill="none" stroke="#fff" stroke-width="1.2"/><path d="M1.5 7h11M7 1.5c-2.5 3-2.5 8 0 11M7 1.5c2.5 3 2.5 8 0 11" fill="none" stroke="#fff" stroke-width="1"/></svg>
    </span>
    www.brightnookclean.example
    <span class="divider">|</span>
    <span class="icon-dot icon-dot--sm">
      <svg width="13" height="10" viewBox="0 0 14 10"><rect x=".7" y=".7" width="12.6" height="8.6" fill="none" stroke="#fff" stroke-width="1.1"/><path d="M.7 .7L7 5.5l6.3-4.8" fill="none" stroke="#fff" stroke-width="1.1"/></svg>
    </span>
    brightnookclean@example.net
  </p>

  <div class="info-band info-band--front">
    <svg width="11" height="14" viewBox="0 0 12 16"><path d="M6 0C2.7 0 0 2.6 0 5.8 0 10 6 16 6 16s6-6 6-10.2C12 2.6 9.3 0 6 0z" fill="#111"/><circle cx="6" cy="5.8" r="2.2" fill="#efefef"/></svg>
    BONDED &amp; INSURED &nbsp;|&nbsp; PINE HOLLOW, CO 80999
  </div>
</section>

<section class="card card--back">
  <div class="sparkle-field" role="img" aria-label="Soft silver backdrop with scattered sparkle stars"></div>

  <p class="script-band script-band--promise">Quality Service Guaranteed</p>

  <ul class="services services--left">
    <li><svg width="14" height="14" viewBox="0 0 14 14"><path d="M7 0L8 6 14 7 8 8 7 14 6 8 0 7 6 6z" fill="var(--leaf)"/></svg>Residential Home Cleaning</li>
    <li><svg width="14" height="14" viewBox="0 0 14 14"><path d="M7 0L8 6 14 7 8 8 7 14 6 8 0 7 6 6z" fill="var(--leaf)"/></svg>Vacation Rental Cleaning</li>
    <li><svg width="14" height="14" viewBox="0 0 14 14"><path d="M7 0L8 6 14 7 8 8 7 14 6 8 0 7 6 6z" fill="var(--leaf)"/></svg>Commercial Cleaning</li>
    <li><svg width="14" height="14" viewBox="0 0 14 14"><path d="M7 0L8 6 14 7 8 8 7 14 6 8 0 7 6 6z" fill="var(--leaf)"/></svg>Carpet Cleaning</li>
    <li><svg width="14" height="14" viewBox="0 0 14 14"><path d="M7 0L8 6 14 7 8 8 7 14 6 8 0 7 6 6z" fill="var(--leaf)"/></svg>Window Cleaning</li>
  </ul>

  <ul class="services services--right">
    <li><svg width="14" height="14" viewBox="0 0 14 14"><path d="M7 0L8 6 14 7 8 8 7 14 6 8 0 7 6 6z" fill="var(--leaf)"/></svg>Property Management</li>
    <li><svg width="14" height="14" viewBox="0 0 14 14"><path d="M7 0L8 6 14 7 8 8 7 14 6 8 0 7 6 6z" fill="var(--leaf)"/></svg>Property Inspections</li>
    <li><svg width="14" height="14" viewBox="0 0 14 14"><path d="M7 0L8 6 14 7 8 8 7 14 6 8 0 7 6 6z" fill="var(--leaf)"/></svg>Property Maintenance</li>
    <li><svg width="14" height="14" viewBox="0 0 14 14"><path d="M7 0L8 6 14 7 8 8 7 14 6 8 0 7 6 6z" fill="var(--leaf)"/></svg>Trash Removal</li>
    <li><svg width="14" height="14" viewBox="0 0 14 14"><path d="M7 0L8 6 14 7 8 8 7 14 6 8 0 7 6 6z" fill="var(--leaf)"/></svg>Concierge Services</li>
  </ul>

  <div class="info-band info-band--back">
    Corinne Hale &amp; Dean Oakley
    <span class="icon-dot icon-dot--sm" style="width:27px;height:27px;margin-left:14px">
      <svg width="11" height="16" viewBox="0 0 14 20"><rect x="2" y="1" width="10" height="18" rx="2" fill="none" stroke="#fff" stroke-width="1.8"/><circle cx="7" cy="16" r="1" fill="#fff"/></svg>
    </span>
    (555)318-2207
  </div>
</section>

</body>
</html>
```